Design of a chocolate packaging

In hand-lettering-style: "Thank you for your work - you are an important part of our team!" (in big letters - almost 2/3 of the whole place) "This chocolate is a lot, so you enter into a raffle and have a great chance of a Zelta Rovo and many more great winnings ... all the information is below www.brv-nordlichtwerk.de! Good luck !!! " (in small letters underneath) The place is: 7,3cm * 15,3cm (crosswise)

Font styles to use
Script

```html
<!DOCTYPE html>
<html lang="de">
<head>
<meta charset="utf-8">
<title>Danke – Schokoladenverpackung</title>
<link rel="stylesheet" href="https://fonts.googleapis.com/css2?family=Sniglet:wght@400;800&family=Open+Sans:wght@400;600&display=swap">
<style>
  :root {
    --backdrop: #cdd6d4;
    --carton: #cba55d;
    --fold: #d8b978;
    --ink: #141210;
    --cocoa: #5a4330;
    --cocoa-edge: #1e1510;
    --url: #6d5a3a;
  }
  html, body {
    margin: 0;
    width: 1200px;
    height: 1000px;
    overflow: hidden;
    background: var(--backdrop);
  }
  .canvas { position: relative; width: 1200px; height: 1000px; }
  .dieline { position: absolute; left: 0; top: 0; }
  .front-panel {
    position: absolute;
    left: 65px; top: 138px;
    width: 320px; height: 670px;
    font-family: "Sniglet", "Comic Sans MS", sans-serif;
    font-variant: small-caps;
    color: var(--ink);
  }
  .line { position: absolute; margin: 0; line-height: 1; white-space: nowrap; }
  .right { right: 25px; text-align: right; }
  .hero {
    color: var(--cocoa);
    font-weight: 800;
    text-shadow: 1px 1px 0 var(--cocoa-edge), 2px 3px 0 var(--cocoa-edge);
  }
  .danke { left: 24px; top: 20px; font-size: 78px; letter-spacing: 1px; }
  .fuer { top: 95px; font-size: 14px; }
  .deine { top: 108px; font-size: 44px; }
  .arbeit { top: 148px; font-size: 44px; }
  .du { left: 22px; top: 196px; font-size: 120px; }
  .bist { top: 283px; font-size: 22px; }
  .ein { top: 315px; font-size: 14px; }
  .wichtiger { top: 330px; font-size: 44px; }
  .teil { top: 382px; font-size: 48px; }
  .unseres { top: 438px; font-size: 14px; }
  .teams { top: 452px; font-size: 44px; }
  .raffle-note {
    position: absolute;
    left: 0; right: 0; top: 554px;
    margin: 0;
    text-align: center;
    font-family: "Open Sans", Arial, sans-serif;
    font-variant: normal;
    font-size: 9.6px;
    line-height: 12.8px;
    color: var(--ink);
  }
  .raffle-note .url { color: var(--url); }
</style>
</head>
<body>
<div class="canvas">
  <svg class="dieline" width="1200" height="1000" viewBox="0 0 1200 1000" aria-hidden="true">
    <g fill="var(--carton)">
      <polygon points="65,110 90,83 360,83 385,110 385,138 65,138"/>
      <polygon points="65,808 385,808 385,835 360,862 90,862 65,835"/>
      <rect x="37" y="138" width="348" height="670"/>
      <polygon points="385,138 730,138 760,165 760,780 730,808 385,808"/>
    </g>
    <g stroke="var(--fold)" stroke-width="1" fill="none">
      <line x1="65" y1="110" x2="385" y2="110"/>
      <line x1="65" y1="138" x2="385" y2="138"/>
      <line x1="65" y1="808" x2="385" y2="808"/>
      <line x1="65" y1="835" x2="385" y2="835"/>
      <line x1="65" y1="138" x2="65" y2="808"/>
      <line x1="385" y1="138" x2="385" y2="808"/>
    </g>
  </svg>

  <div class="front-panel">
    <p class="line hero danke">Danke</p>
    <p class="line right fuer">für</p>
    <p class="line right deine">Deine</p>
    <p class="line right arbeit">Arbeit</p>
    <p class="line hero du">Du</p>
    <p class="line right bist">bist</p>
    <p class="line right ein">ein</p>
    <p class="line right wichtiger">wichtiger</p>
    <p class="line right teil">Teil</p>
    <p class="line right unseres">unseres</p>
    <p class="line right teams">Teams!</p>
    <p class="raffle-note">
      Diese Schokolade ist ein Los.<br>
      Du nimmst damit an einer Verlosung Teil<br>
      und hast großartige Chancen<br>
      auf einen Zelta Rovo und viele weitere tolle Gewinne...<br>
      alle Infos gibt es unter<br>
      <span class="url">www.brv-nordlichtwerk.de</span><br>
      Viel Glück!!!
    </p>
  </div>
</div>
</body>
</html>
```